New Business Card Design Project

I would like my card design to look exactly like the logo, design, layout, and print of the current attached file. The only change I would like made would be for the print to say THE KMW GROUP instead of THE HALLORAN GROUP. Basically, just replace his group name with my group name. I would also like the backgroud to be the same texture and color as the attached file. I love the dark blue lettering and house logo on the card.

I am completely open to the rest of the card design. I just want something clean and simple. Only basic contact info required on the card. Maybe just name: Kyle M Warrick and cell # 555.914.2087 and email kyle@orchidhomesagent.com

```html
<!DOCTYPE html>
<html lang="en">
<head>
<meta charset="UTF-8">
<title>The KMW Group – Business Card</title>
<link rel="stylesheet" href="https://fonts.googleapis.com/css2?family=Montserrat:wght@400&family=Open+Sans:wght@400;600&display=swap">
<style>
  :root {
    --backdrop: #e9e9ea;
    --card-paper: #f7f7f5;
    --navy: #171a38;
    --on-navy: #ffffff;
  }
  * { margin: 0; padding: 0; box-sizing: border-box; }
  html, body {
    width: 1200px;
    height: 900px;
    overflow: hidden;
    background: var(--backdrop);
  }
  .card {
    position: absolute;
    left: 150px;
    top: 193px;
    width: 900px;
    height: 514px;
    background: var(--card-paper);
    overflow: hidden;
  }
  .brand {
    position: absolute;
    left: 50%;
    top: 24%;
    transform: translateX(-50%);
    display: flex;
    align-items: center;
    gap: 28px;
  }
  .brand-square {
    width: 86px;
    height: 86px;
    background: var(--navy);
  }
  .brand-name {
    font-family: "Montserrat", sans-serif;
    font-weight: 400;
    font-size: 33px;
    line-height: 1.12;
    letter-spacing: 0.14em;
    color: var(--navy);
    white-space: nowrap;
  }
  .contact-band {
    position: absolute;
    left: 0;
    right: 0;
    top: 64%;
    height: 26%;
    background: var(--navy);
    color: var(--on-navy);
  }
  .agent-name {
    position: absolute;
    left: 68px;
    top: 50%;
    transform: translateY(-50%);
    padding-left: 10px;
    border-left: 3px solid var(--on-navy);
    font-family: "Open Sans", sans-serif;
    font-weight: 600;
    font-size: 40px;
    line-height: 1.1;
    white-space: nowrap;
  }
  .contact-list {
    position: absolute;
    left: 512px;
    top: 50%;
    transform: translateY(-50%);
    list-style: none;
    font-family: "Montserrat", sans-serif;
    font-size: 19px;
    line-height: 1.5;
    white-space: nowrap;
  }
  .contact-item {
    display: flex;
    align-items: center;
    gap: 8px;
  }
  .contact-icon {
    flex: none;
    width: 17px;
    height: 17px;
    fill: var(--on-navy);
  }
</style>
</head>
<body>
  <section class="card">
    <div class="brand">
      <div class="brand-square"></div>
      <div class="brand-name">THE<br>KMW<br>GROUP</div>
    </div>

    <div class="contact-band">
      <p class="agent-name">Kyle M Warrick</p>
      <ul class="contact-list">
        <li class="contact-item">
          <svg class="contact-icon" viewBox="0 0 24 24" aria-hidden="true">
            <path d="M6.6 10.8a15.1 15.1 0 0 0 6.6 6.6l2.2-2.2a1 1 0 0 1 1-.25 11.4 11.4 0 0 0 3.6.57 1 1 0 0 1 1 1V20a1 1 0 0 1-1 1A17 17 0 0 1 3 4a1 1 0 0 1 1-1h3.5a1 1 0 0 1 1 1c0 1.25.2 2.45.57 3.57a1 1 0 0 1-.25 1z"/>
          </svg>
          <span>| 555.914.2087</span>
        </li>
        <li class="contact-item">
          <svg class="contact-icon" viewBox="0 0 24 24" aria-hidden="true">
            <path d="M2 5h20v14H2z M2 5l10 8 10-8" fill="var(--on-navy)" stroke="var(--navy)" stroke-width="1.6"/>
          </svg>
          <span>| kyle@orchidhomesagent.com</span>
        </li>
      </ul>
    </div>
  </section>
</body>
</html>
```